A unique communication angle to crowdfunding

Looking for a fresh redesign of a crowd funding website that deals in real estate. I already have the content, but am looking to take the design to the next level.

Existing real estate crowd funding sites focus on the real estate. I want to explore communication angle that:
- puts the investor in the centre of the communication: "become a baron"
- highlights the international nature (international properties, international investors)

There's also quite a lot of copy on the site, as we need to explain the service in quite a bit of detail. There's room to reduce the copy and replace with graphics. Could also consider clicking to see different text (see our difference section in http://galatownfeed.com)

The backend of the platform is already being worked on by a specialist crowd funding service provider.

In total there are 5 pages to be designed.

The homepage is really important. Right now it looks quite dated. It doesn't have a great layout. Note there is no mobile version of the website, so the pages need to be seen well on mobile devices. When looking at the brief, refer to the following links too:

current website:
http://pooltenant.com

some revisions made so far:
http://preview.fundmerrow.com/2G5GO2

Attached are logo files and another file which contained copy for the pages. No need to rework the logo.

Please make sure to use the same copy in the brief on the webpages, to ensure the layouts work. Designers are free to propose images they feel work on the pages.

I would like to see if rather than tweaking the pages, it's possible to come up with a better design concept. If the 5 pages are accepted, there's a chance I'll request an additional 4 pages.
Updates

Please note the font used in the logo is called "harabara" in case you decide to use it in any of the titles, etc.

Please note there is one additional page for which we would like to review designs. Note the page would be a template to be used on all future real estate detail pages. Here is an example of the current design for reference:

http://pooltenant.com/projects/view/14

In total there are 5 page designs required, (homepage + 4)

Thank you

FYI -

Just a quick note to give information from similar UK real estate crowdfunding sites:
http://www.estatewren.co.uk
http://plotharbor.co.uk
https://www.tilgarcap.com

Of the above, only plotharbor has a nice clean looking landing page. Information is clear and well laid out.

Hi all, just uploaded a new file in the brief. Contains some comments and a website reference. I thought it may help to explain how we could convey international aspect as well as how we could convey images in a more modern way. This is an option you can consider, but its entirely up to you how how answer the brief. Thanks!

We would like to let you know that we have just shortlisted the best designs. Together with that, we have also passed some detailed feedback to all designers who weren't shortlisted. If we didn't contact you, please let us know. If you haven't submitted a design or are working on revisions, please note these will no longer be taken into account now. We hope you understand that we need to close the project today. Thank you all once again for your great work and design concepts. Here's hoping we meet again on a future design brief. Cheers, pooltenant team.

Target Market(s)

At the moment, only rich are able to buy real estate. With this service, anyone can become a landlord. Target buyers:

Young professionals, looking to diversify from stock market and lower risk
People nearing retirement, looking for stable rental incomes
Retirees - looking to supplement pensions with possibility of capital gains
Parents - looking for a way to save long term for their children (instead of low interest paying bank accounts)

Industry/Entity Type

Communication

Font styles to use
Sans Serif
Other font styles liked:
• harabara

Colors
add136
f5f9eb
959595
000000

Requirements
Must have
• Overall, the site must convey "whoever you are, you too can become a landlord", and that you don't need to be wealthy to invest in real estate. See

Communication should put the investor (or the baron) at the centre. The investor can be any of those described in the target market.

Show the aspirational side of property ownership.

In addition to the investor/baron character, the second main theme is international. No other real estate crowdfunding website highlights this.
Nice to have
• Banner could show different consumer types, to illustrate that the service can appeal to many different profiles. Refer to attached file "home page reference - plainasdew.com" as an example of how this could be done.

Aim to show the international side of the service. Properties around the world, investors around the world.

```html
<!DOCTYPE html>
<html lang="en">
<head>
<meta charset="utf-8">
<title>Pooltenant – Become a Baron</title>
<link rel="stylesheet" href="https://fonts.googleapis.com/css2?family=Open+Sans:wght@400;600;700&family=Roboto:wght@400;700;900&family=Varela+Round&display=swap">
<style>
:root{
  --green:#add136;
  --green-dark:#8fbb2a;
  --green-light:#c7e05c;
  --tint:#f5f9eb;
  --grey:#959595;
  --grey-dark:#6a6a6a;
  --grey-box:#6f6f6f;
  --ink:#000;
  --paper:#f2f2f2;
  --clients-bg:#e8e8e8;
  --bar:#6b6b6b;
  --footer:#3b3b3b;
  --white:#fff;
}
*{box-sizing:border-box;margin:0;padding:0}
html,body{width:723px;height:1200px;overflow:hidden}
body{position:relative;background:var(--paper);font-family:"Open Sans",Arial,sans-serif;color:var(--grey)}
.section{position:absolute;left:0;width:723px}

/* header */
.site-header{top:0;height:54px;background:var(--white);z-index:3;box-shadow:0 1px 3px rgba(0,0,0,.25)}
.nav-band{position:absolute;right:0;top:0;width:448px;height:54px;background:linear-gradient(90deg,var(--green-light),var(--green));clip-path:polygon(42px 0,100% 0,100% 100%,0 100%)}
.brand{position:absolute;left:101px;top:13px;display:flex;align-items:center;gap:6px}
.brand-dot{width:22px;height:22px;border-radius:50%;background:var(--green)}
.brand-name{font-family:"Varela Round",sans-serif;font-size:18px;color:var(--green-dark)}
.main-nav{position:absolute;right:0;top:0;height:54px;width:430px;display:flex;align-items:center;justify-content:flex-end;gap:22px;padding-right:97px}
.main-nav a{font-size:8px;font-weight:600;color:var(--white);text-decoration:none;white-space:nowrap}

/* hero */
.hero{top:54px;height:252px;background:linear-gradient(180deg,#9fb7c4 0%,#7f9a6a 30%,#6d7c4a 55%,#9a8a76 80%,#7a6e60 100%)}
.hero-photo-note{position:absolute;inset:0}
.hero-title{position:absolute;left:101px;top:88px;color:var(--white);font-family:"Roboto",sans-serif;text-shadow:0 1px 3px rgba(0,0,0,.35)}
.hero-title .small{display:block;font-size:19px;font-weight:400;letter-spacing:.5px;line-height:1}
.hero-title .big{display:block;font-size:62px;font-weight:700;line-height:.95;letter-spacing:-1px}

/* pitch band */
.pitch{top:306px;height:167px;background:linear-gradient(180deg,rgba(173,209,54,.95),rgba(160,200,50,.95));text-align:center;color:var(--white)}
.pitch h1{font-family:"Varela Round",sans-serif;font-weight:400;font-size:23px;line-height:27px;margin-top:15px;letter-spacing:-.3px}
.pitch p{font-size:12.6px;line-height:16.5px;margin-top:10px}

/* projects */
.projects{top:473px;height:211px;background:var(--paper)}
.intro-heading{position:absolute;left:102px;top:28px;width:187px;height:29px;background:var(--grey-box);color:var(--white);font-family:"Varela Round",sans-serif;font-size:16.5px;line-height:29px;padding-left:8px}
.intro-col{position:absolute;top:73px;width:78px;font-size:6px;line-height:12.6px;color:#a8a8a8}
.intro-col.first{left:103px}
.intro-col.second{left:204px;border-left:1px solid #ddd;padding-left:0;left:190px;padding-left:14px;width:96px}
.project{position:absolute;top:28px;width:140px}
.project.one{left:317px}
.project.two{left:484px}
.project-photo{width:138px;height:86px;border:3px solid #e2e2e2}
.project.one .project-photo{background:linear-gradient(180deg,#6f9fd4 0%,#a9c6e4 45%,#d8d2bd 70%,#8a8d86 100%)}
.project.two .project-photo{background:linear-gradient(180deg,#1d3a7a 0%,#3a5a8f 35%,#c9a66b 60%,#2aa8e0 85%,#1577b5 100%)}
.funding{position:absolute;top:95px;left:0;display:flex;gap:5px}
.funding svg{display:block}
.legend{margin-top:8px;font-size:6.2px;line-height:8px;color:var(--grey-dark)}
.legend .row{display:flex;align-items:center;gap:4px;margin-bottom:3px;font-weight:600}
.legend .row.pledged{color:var(--green)}
.legend .sw{width:6px;height:6px;display:inline-block}
.legend .sw.g{background:var(--green)}
.legend .sw.d{background:var(--grey-dark)}
.legend p{margin-top:3px;width:70px;color:#888;font-size:6px;line-height:7.4px}

/* clients */
.clients{top:684px;height:203px;background:var(--clients-bg)}
.clients h2{position:absolute;left:108px;top:27px;font-family:"Varela Round",sans-serif;font-weight:400;font-size:17px;color:var(--green)}
.client{position:absolute;font-family:"Roboto",sans-serif;font-weight:700;color:#8a8a8a;display:flex;align-items:center;gap:5px;white-space:nowrap}
.client .mark{width:9px;height:9px;background:#9a9a9a;border-radius:50%}

/* testimonial */
.testimonial{top:887px;height:212px;background:var(--paper)}
.portrait{position:absolute;left:108px;top:32px;width:120px;height:120px;border-radius:50%;border:4px solid #fff;box-shadow:0 0 0 1px #ddd;background:radial-gradient(circle at 50% 40%,#e0a070 0%,#d68a58 30%,#5e8a3a 60%,#3f6a2a 100%)}
.quote-marks{position:absolute;font-family:"Roboto",sans-serif;font-weight:900;color:#d6d6d6;font-size:76px;line-height:1}
.quote-marks.open{left:240px;top:30px}
.quote-marks.close{left:506px;top:140px}
.quote-text{position:absolute;left:277px;top:37px;width:340px;font-size:12.3px;line-height:15.3px;color:#a0a0a0}
.author{position:absolute;left:117px;top:156px}
.author .name{font-size:13px;color:#555}
.author .role{font-size:6.3px;color:#666}

/* contact bar */
.contact-bar{top:1099px;height:38px;background:var(--bar);color:var(--white);font-size:6.3px}
.contact-item{position:absolute;top:0;height:38px;display:flex;align-items:center;gap:5px}
.social-dot{width:8px;height:8px;border-radius:50%;background:var(--white);display:inline-block}

/* footer */
.site-footer{top:1137px;height:63px;background:var(--footer)}
.footer-brand{position:absolute;left:103px;top:14px;display:flex;align-items:center;gap:6px}
.footer-brand .brand-dot{background:#cfcfcf}
.footer-brand .brand-name{color:#cfcfcf}
.copyright{position:absolute;left:135px;top:43px;font-size:5.8px;color:#aaa}
.footer-nav{position:absolute;right:97px;top:32px;font-size:6.8px;color:var(--white)}
.footer-nav a{color:var(--white);text-decoration:none}
</style>
</head>
<body>

<header class="section site-header">
  <div class="brand"><span class="brand-dot"></span><span class="brand-name">pooltenant</span></div>
  <div class="nav-band"></div>
  <nav class="main-nav">
    <a href="#">About</a><a href="#">How It Works</a><a href="#">Discover a Project</a><a href="#">The Baron Blog</a><a href="#">Contact</a>
  </nav>
</header>

<section class="section hero">
  <div class="hero-photo-note" role="img" aria-label="Photo of a young couple embracing in front of a large suburban house among trees"></div>
  <h2 class="hero-title"><span class="small">BECOME A</span><span class="big">BARON</span></h2>
</section>

<section class="section pitch">
  <h1>Reconstructing a property ladder<br>that's strong and fair</h1>
  <p>By harnessing the power of crowds, it's possible to become a landlord in locations<br>around the world. Forget the burden of financing 100% of the purchase.<br>Leave the day to day management of your property portfolio to us.<br>Start with 1% in a project and plan your steps to becoming a true baron</p>
</section>

<section class="section projects">
  <h2 class="intro-heading">Together we can buy</h2>
  <p class="intro-col first">Pellentesque sagittis leo sed aliquam vulputate. Interdum et malesuada fames ac ante ipsum primis in faucibus. Sed dapibus auctor nunc, et ornare nibh. Praesent nibh risus, commodo</p>
  <p class="intro-col second">Pellentesque sagittis leo sed aliquam vulputate. Interdum et malesuada fames ac ante ipsum primis in faucibus. Sed dapibus auctor nunc, et ornare nibh. Praesent nibh risus, commodo</p>

  <article class="project one">
    <div class="project-photo" role="img" aria-label="Photo of a row of cream townhouses under a blue sky"></div>
    <div class="funding">
      <svg width="66" height="66" viewBox="0 0 66 66" aria-label="Pledged 76 percent, invested 24 percent">
        <circle cx="33" cy="33" r="25" fill="none" stroke="var(--grey-dark)" stroke-width="14"/>
        <circle cx="33" cy="33" r="25" fill="none" stroke="var(--green)" stroke-width="14" stroke-dasharray="119.4 157" transform="rotate(-3 33 33) scale(-1 1) translate(-66 0)"/>
        <text x="22" y="11" font-size="5.5" fill="#fff" font-family="Open Sans,sans-serif" font-weight="700">24%</text>
        <text x="41" y="62" font-size="5.5" fill="#fff" font-family="Open Sans,sans-serif" font-weight="700">76%</text>
      </svg>
      <div class="legend">
        <div class="row pledged"><span class="sw g"></span>Pledged 76%</div>
        <div class="row"><span class="sw d"></span>Invested 24%</div>
        <p>sed aliquam vulputate. Interdum et malesuada.</p>
      </div>
    </div>
  </article>

  <article class="project two">
    <div class="project-photo" role="img" aria-label="Photo of a villa with a lit swimming pool at dusk"></div>
    <div class="funding">
      <svg width="66" height="66" viewBox="0 0 66 66" aria-label="Pledged 76 percent, invested 24 percent">
        <circle cx="33" cy="33" r="25" fill="none" stroke="var(--grey-dark)" stroke-width="14"/>
        <circle cx="33" cy="33" r="25" fill="none" stroke="var(--green)" stroke-width="14" stroke-dasharray="119.4 157" transform="rotate(-3 33 33) scale(-1 1) translate(-66 0)"/>
        <text x="22" y="11" font-size="5.5" fill="#fff" font-family="Open Sans,sans-serif" font-weight="700">24%</text>
        <text x="41" y="62" font-size="5.5" fill="#fff" font-family="Open Sans,sans-serif" font-weight="700">76%</text>
      </svg>
      <div class="legend">
        <div class="row pledged"><span class="sw g"></span>Pledged 76%</div>
        <div class="row"><span class="sw d"></span>Invested 24%</div>
        <p>sed aliquam vulputate. Interdum et malesuada.</p>
      </div>
    </div>
  </article>
</section>

<section class="section clients">
  <h2>Our Clients</h2>
  <div class="client" style="left:110px;top:63px;font-size:9px"><span class="mark"></span>Harbour Ledger</div>
  <div class="client" style="left:245px;top:70px;font-size:12px">Orbit Tech Daily</div>
  <div class="client" style="left:398px;top:70px;font-size:10px">Crowd Forum Week</div>
  <div class="client" style="left:508px;top:67px;font-size:15px">Coinwise</div>
  <div class="client" style="left:110px;top:110px;font-size:13px">Yonder Finance</div>
  <div class="client" style="left:243px;top:110px;font-size:15px">South Bay Morning Courier</div>
  <div class="client" style="left:509px;top:108px;font-size:10px"><span class="mark" style="border-radius:0;width:12px;height:12px"></span>Launchpad Kowloon</div>
  <div class="client" style="left:110px;top:152px;font-size:14px">Radio Eastgate</div>
  <div class="client" style="left:245px;top:156px;font-size:9px"><span class="mark"></span>crowdcircle.net</div>
</section>

<section class="section testimonial">
  <div class="portrait" role="img" aria-label="Portrait photo of a smiling man in an orange shirt"></div>
  <span class="quote-marks open">&ldquo;</span>
  <p class="quote-text">Donec vitae felis nec magna condimentum porttitor ac eu massa. Donec ut venenatis lorem. Cras ullamcorper est nec consectetur consequat. Donec pellentesque lobortis leo ac ultrices. Aenean in urna vitae nunc porttitor laoreet. Nulla sollicitudin dictum mauris nec luctus. Sed tellus orci, cursus dictum semper vel, imperdiet in metus. Nunc placerat congue lacinia. Nullam ac lectus orci. In eleifend augue at sollicitudin tristique. Duis nec nisi ornare,</p>
  <span class="quote-marks close">&rdquo;</span>
  <div class="author"><p class="name">Donec Vitae</p><p class="role">Brand Manager Hartwell &amp; Co. Ltd</p></div>
</section>

<section class="section contact-bar">
  <div class="contact-item" style="left:103px">Follow Us <span class="social-dot"></span><span class="social-dot"></span></div>
  <div class="contact-item" style="left:194px">
    <svg width="10" height="7" viewBox="0 0 10 7"><rect x=".5" y=".5" width="9" height="6" fill="none" stroke="#fff"/><path d="M.5 .5 5 4 9.5 .5" fill="none" stroke="#fff"/></svg>
    rowan@larkmail.net</div>
  <div class="contact-item" style="left:294px">
    <svg width="10" height="10" viewBox="0 0 10 10"><circle cx="5" cy="5" r="4.5" fill="none" stroke="#fff"/><path d="M3.4 2.8c.3 1.8 1.5 3.2 3.2 3.8l.6-.8" fill="none" stroke="#fff" stroke-width="1.1"/></svg>
    +852 2790 4418</div>
  <div class="contact-item" style="left:384px">
    <svg width="11" height="10" viewBox="0 0 11 10"><path d="M5.5 .5 10.5 5H9v4.5H6.5V6.5h-2v3H2V5H.5z" fill="#fff"/></svg>
    Suite 902, Block B, Harbourline Centre 118 Keel Street Kowloon, Hong Kong</div>
</section>

<footer class="section site-footer">
  <div class="footer-brand"><span class="brand-dot"></span><span class="brand-name">pooltenant</span></div>
  <p class="copyright">© 2014 Pooltenant. All rights reserved</p>
  <nav class="footer-nav"><a href="#">About</a> - <a href="#">How it Works</a> - <a href="#">Discover a project</a> - <a href="#">The Baron Blog</a> - <a href="#">Contact</a></nav>
</footer>

</body>
</html>
```